PennacottHoldings.com Website Design

Simple website using existing logo. See "free website" already up. Want something much more professional and dynamic. Purpose is to describe my business and give me a place to post and update projects as they move along. Need to be able to post links to other companies that my firm invests equity in.
Target Market(s)
Banks, Financial Advisors
Industry/Entity Type
It Professional
Number of Pages Required
4 page
Font styles to use
Sans Serif
Requirements
Must have
- Ability to add and edit projects so they appear in the order of most current to oldest.
Nice to have
- Page to blog and link to facebook page

```html
<!DOCTYPE html>
<html lang="en">
<head>
<meta charset="utf-8">
<title>Pennacott Holdings</title>
<link href="https://fonts.googleapis.com/css2?family=Open+Sans:wght@400;600;700;800&display=swap" rel="stylesheet">
<style>
:root{
  --red:#e1161c;
  --red-dark:#c40f14;
  --ink:#222;
  --muted:#777;
  --grey-band:#ececec;
  --logo-grey:#9a9a9a;
  --footer:#0b0b0b;
  --white:#fff;
}
*{box-sizing:border-box;margin:0;padding:0}
html,body{width:829px;height:1200px;overflow:hidden;background:var(--white)}
body{font-family:"Open Sans",Arial,sans-serif;color:var(--ink);position:relative}
.site-header{height:50px;display:flex;align-items:center;justify-content:space-between;padding:0 120px 0 130px}
.brand{display:flex;align-items:center;gap:7px;color:var(--red);font-weight:800;font-size:17px;letter-spacing:.2px}
.brand-mark{width:16px;height:16px;background:var(--red);border-radius:50%}
.main-nav{display:flex;gap:22px;font-size:8.5px;font-weight:600;letter-spacing:.4px}
.main-nav a{color:var(--ink);text-decoration:none;padding-bottom:4px}
.main-nav a.active{color:var(--red);border-bottom:2px solid var(--red)}
.hero{position:relative;height:322px;text-align:center;color:var(--white)}
.hero-photo{position:absolute;inset:0;background:linear-gradient(180deg,#0d1a33 0%,#2a3f6d 40%,#3b2a5e 62%,#13203a 80%,#0a1222 100%)}
.hero-text{position:absolute;left:0;right:0;top:205px}
.hero-kicker{font-size:17px;font-weight:700;letter-spacing:1px}
.hero-title{font-size:28px;font-weight:800;letter-spacing:1px;margin-top:2px}
.hero-dots{position:absolute;left:0;right:0;bottom:22px;display:flex;justify-content:center;gap:6px}
.hero-dots span{width:8px;height:8px;border-radius:50%;background:var(--white)}
.about{text-align:center;padding:24px 130px 0}
.section-title{font-size:25px;font-weight:600;color:#333}
.about p{font-size:7.5px;line-height:1.6;color:var(--muted);margin-top:10px}
.about p+p{margin-top:8px}
.services{background:var(--red);margin-top:22px;height:176px;padding:26px 132px 0;display:flex;gap:14px}
.service{flex:1;text-align:center;color:var(--white)}
.service-photo{height:70px}
.service h3{font-size:13px;font-weight:700;margin-top:8px}
.service p{font-size:7px;line-height:1.5;margin-top:3px;padding:0 10px;opacity:.9}
.btn{display:inline-block;margin-top:8px;border:1px solid var(--white);font-size:7px;font-weight:700;padding:3px 10px;color:var(--white);letter-spacing:.3px}
.partners{background:var(--grey-band);height:60px;margin-top:10px;display:flex;align-items:center;justify-content:center;gap:34px}
.partner-badge{width:58px;height:14px;background:var(--logo-grey);border-radius:2px}
.projects{padding:26px 130px 0}
.projects .section-title{font-size:17px}
.project-list{display:flex;gap:30px;margin-top:14px}
.project{flex:1;display:flex;gap:10px}
.project-photo{width:120px;height:72px;flex:none}
.project h4{font-size:9px;font-weight:600;color:#333}
.project p{font-size:7px;line-height:1.5;color:var(--muted);margin-top:3px}
.project a{display:block;font-size:7px;font-weight:700;color:var(--red);margin-top:4px;text-decoration:none}
.site-footer{position:absolute;left:0;right:0;bottom:0;height:85px;background:var(--footer);color:var(--white);padding:20px 130px 0}
.footer-row{display:flex;justify-content:space-between;align-items:flex-start}
.footer-nav{display:flex;gap:14px;font-size:8px;font-weight:600}
.footer-contact{font-size:7px;line-height:1.8;color:#ccc}
.footer-contact div{display:flex;align-items:center;gap:5px}
.social{display:flex;gap:6px;margin-top:4px}
.social span{width:9px;height:9px;border-radius:50%;background:var(--white)}
.copyright{font-size:6.5px;color:#888;margin-top:8px}
</style>
</head>
<body>
<header class="site-header">
  <div class="brand"><span class="brand-mark"></span>Pennacott Holdings</div>
  <nav class="main-nav">
    <a class="active" href="#">HOME</a><a href="#">ABOUT US</a><a href="#">SERVICES</a><a href="#">PROJECTS</a><a href="#">CONTACT</a>
  </nav>
</header>

<section class="hero">
  <div class="hero-photo" role="img" aria-label="Illuminated arch bridge over a river at dusk with a city skyline"></div>
  <div class="hero-text">
    <div class="hero-kicker">LOREM IPSUM DOLOR AMET CONSECTET</div>
    <div class="hero-title">MAURIS VITAE VESTIBULUM</div>
  </div>
  <div class="hero-dots"><span></span><span></span><span></span><span></span></div>
</section>

<section class="about">
  <h2 class="section-title">About Pennacott Holdings</h2>
  <p>Pennacott Holdings is a private equity firm that partners with growing companies across technology and services. We provide patient capital, practical guidance and a long term view, helping founders build stronger businesses while giving banks and advisors a trusted partner for every stage of growth.</p>
  <p>Our team combines decades of finance and operating experience. We review each opportunity with care, invest alongside management and report progress openly so clients always know where their projects stand.</p>
</section>

<section class="services">
  <div class="service">
    <div class="service-photo" role="img" aria-label="Business team meeting around a table" style="background:linear-gradient(135deg,#c9d3dc,#8fa0b0)"></div>
    <h3>Why Choose Us</h3>
    <p>We bring clear thinking, honest advice and steady capital to every partnership we form.</p>
    <span class="btn">READ MORE</span>
  </div>
  <div class="service">
    <div class="service-photo" role="img" aria-label="Investors reviewing financial documents" style="background:linear-gradient(135deg,#b8c4cf,#6f7f90)"></div>
    <h3>Investment Service</h3>
    <p>We invest equity in proven firms with strong teams and a clear path to growth.</p>
    <span class="btn">READ MORE</span>
  </div>
  <div class="service">
    <div class="service-photo" role="img" aria-label="Modern glass office building" style="background:linear-gradient(135deg,#a9c7de,#4f7595)"></div>
    <h3>How We Work</h3>
    <p>We study each deal, agree on goals together and track results at every step.</p>
    <span class="btn">READ MORE</span>
  </div>
</section>

<section class="partners" aria-label="Portfolio companies">
  <span class="partner-badge"></span><span class="partner-badge"></span><span class="partner-badge"></span><span class="partner-badge"></span><span class="partner-badge"></span><span class="partner-badge"></span>
</section>

<section class="projects">
  <h2 class="section-title">Latest Projects</h2>
  <div class="project-list">
    <article class="project">
      <div class="project-photo" role="img" aria-label="New residential housing development" style="background:linear-gradient(180deg,#8fb4d6,#b7a58a)"></div>
      <div>
        <h4>Integer congue augue</h4>
        <p>A mixed use development funded with local partners, now in its second phase of construction.</p>
        <a href="#">Read More</a>
      </div>
    </article>
    <article class="project">
      <div class="project-photo" role="img" aria-label="Row of renovated townhouses" style="background:linear-gradient(180deg,#9cc0e0,#a58f78)"></div>
      <div>
        <h4>Cum sociis natoque</h4>
        <p>Residential renovation project in progress, with final units expected to be completed this year.</p>
        <a href="#">Read More</a>
      </div>
    </article>
  </div>
</section>

<footer class="site-footer">
  <div class="footer-row">
    <nav class="footer-nav"><span>HOME</span><span>TEAM</span><span>ADVISORS</span><span>SERVICES</span><span>PROJECTS</span><span>CONTACT</span></nav>
    <div class="footer-contact">
      <div><svg width="7" height="7" viewBox="0 0 10 10"><path d="M2 1l2 2-1 1.5c.8 1.4 1.8 2.4 3 3L7.5 6l2 2-1.5 1.5C4 9 1 6 .5 2z" fill="#ccc"/></svg>(604) 555-0148</div>
      <div><svg width="7" height="7" viewBox="0 0 10 10"><rect x=".5" y="2" width="9" height="6" fill="none" stroke="#ccc"/><path d="M.5 2l4.5 3.5L9.5 2" fill="none" stroke="#ccc"/></svg>info@pennacottholdings.com</div>
    </div>
    <div class="social"><span></span><span></span><span></span></div>
  </div>
  <div class="copyright">© 2015 Pennacott Holdings. All rights reserved.</div>
</footer>
</body>
</html>
```